Web Design Project

We are looking to for a redesign for www.valtemo.com. Valtemo Systems is a Managed Service Provider of IT solutions based is Calgary, Alberta, Canada. We are currently expanding into the Edmonton market and would like to lauch our new site with our expansion.
The design should be sleak in style and communicate a professional vision to our clients and prospects.

Thanks,
Owen

Target Market(s)

Small to medium size businesses looking to outsource or complement their IT solutions.

Industry/Entity Type

It Professional

```html
<!DOCTYPE html>
<html lang="en">
<head>
<meta charset="utf-8">
<title>Valtemo Systems – Managed IT Service Professionals</title>
<link href="https://fonts.googleapis.com/css2?family=Source+Sans+3:wght@300;400;600&display=swap" rel="stylesheet">
<style>
:root{
  --red:#c4121a;
  --ink:#111;
  --text:#333;
  --muted:#555;
  --pill:#e0e0e0;
  --rule:#9a9a9a;
  --line:#d8d8d8;
  --white:#fff;
}
*{box-sizing:border-box;margin:0;padding:0}
html,body{width:1200px;height:1087px;overflow:hidden;background:var(--white)}
body{position:relative;font-family:"Source Sans 3",sans-serif;color:var(--text);font-size:12px}
.abs{position:absolute}
.topbar{left:0;top:0;width:1200px;height:4px;background:var(--ink)}
.header-band{left:0;top:4px;width:1200px;height:405px;background:linear-gradient(#f2f2f2,#fff 40%,#fff 70%,#e6e6e6)}
.contact-tab{left:957px;top:0;width:80px;height:28px;background:var(--ink);color:#fff;font-size:12px;line-height:30px;text-align:center}
.brand{left:168px;top:24px;display:flex;align-items:center;gap:10px}
.brand-mark{width:38px;height:38px;background:var(--red)}
.brand-name{font-size:38px;font-weight:400;letter-spacing:4px;color:var(--ink);line-height:1}
.nav{left:635px;top:44px;display:flex;gap:5px}
.nav a{display:block;width:97px;height:28px;background:var(--ink);color:#fff;text-decoration:none;text-align:center;line-height:28px;font-size:12px;border-radius:2px;position:relative}
.nav a.active{background:var(--red)}
.nav a.active::after{content:"";position:absolute;left:44px;bottom:-6px;border:5px solid transparent;border-top-color:var(--red);border-bottom:0}
.slider-frame{left:174px;top:92px;width:864px;height:317px;background:#e4e4e4}
.slider-shadow{left:340px;top:403px;width:530px;height:20px;background:radial-gradient(ellipse at top,rgba(0,0,0,.35),rgba(0,0,0,0) 70%)}
.slider-photo{left:183px;top:100px;width:848px;height:301px;background:linear-gradient(90deg,#4b5663 0%,#8c97a2 35%,#c9ced6 60%,#dfe2e7 100%)}
.caption{left:248px;top:212px;width:267px;height:74px;background:rgba(235,235,235,.85);padding:8px 0 0 18px;font-size:28px;font-weight:300;line-height:28px;color:#222;white-space:nowrap;letter-spacing:-.3px}
.arrow{width:35px;height:35px;background:#fff;display:flex;align-items:center;justify-content:center}
.feature h2,.section-title{font-weight:300;color:var(--red);font-size:27px;line-height:1}
.feature p{margin-top:15px;font-size:12px;line-height:18.5px;color:var(--text)}
.feature-icon{width:70px;height:70px;border-radius:50%;border:1px solid #d0d0d0;background:#fff;display:flex;align-items:center;justify-content:center}
.feature-icon span{width:56px;height:56px;border-radius:50%;background:#e6e6e6;display:flex;align-items:center;justify-content:center}
.btn-more{width:89px;height:27px;background:var(--pill);border-radius:3px;display:flex;align-items:center;justify-content:space-between;padding:0 7px;font-size:12px;color:#444}
.dot{width:15px;height:15px;border-radius:50%;background:#777;display:flex;align-items:center;justify-content:center}
.vrule{border-left:1px dotted var(--rule)}
.hrule{border-top:1px dotted var(--rule);height:0}
.intro{font-size:12px;line-height:18.5px}
.service-list{list-style:none}
.service-list li{width:250px;height:28px;background:var(--pill);margin-bottom:10px;display:flex;align-items:center;gap:13px;padding-left:14px;font-size:13px;color:#333}
.network-art{left:452px;top:752px;width:236px;height:97px;background:linear-gradient(#fff,#eef4f8 60%,#fff)}
.card{background:#fff;border:1px solid #e2e2e2;box-shadow:0 1px 3px rgba(0,0,0,.15)}
.card-title{font-size:19px;font-weight:300;color:var(--red)}
.card small{display:block;font-size:12px;line-height:15px;color:var(--text)}
.card a{color:var(--red);text-decoration:none;font-size:12px}
.portrait{position:absolute;right:0;top:0;width:128px;height:100%;background:linear-gradient(90deg,rgba(255,255,255,0),#c9b29c 45%,#33393f 100%)}
.social{display:flex;align-items:center;height:100%}
.social .label{font-size:12px;margin:0 18px 0 22px}
.social i{display:block;width:37px;height:100%;border-left:1px solid #ececec;display:flex;align-items:center;justify-content:center}
.social i b{display:block;width:18px;height:18px;border-radius:3px;background:#8a8a8a}
.news{left:325px;top:953px;width:715px;height:37px;border:1px solid var(--line);display:flex;align-items:center;font-size:12px}
.news .tag{margin-left:5px;width:56px;height:23px;background:var(--pill);color:var(--red);display:flex;align-items:center;justify-content:center}
.footer{left:178px;top:1008px;width:862px;height:38px;border:1px solid var(--line);display:flex;align-items:center;justify-content:space-between;padding:0 14px;font-size:11px;color:#444}
.footer nav span{margin:0 6px}
.bottombar{left:0;top:1085px;width:1200px;height:2px;background:var(--ink)}
</style>
</head>
<body>
<div class="abs header-band"></div>
<div class="abs topbar"></div>
<div class="abs contact-tab">Contact Us</div>

<div class="abs brand"><span class="brand-mark"></span><span class="brand-name">VALTEMO</span></div>

<nav class="abs nav">
  <a class="active" href="#">Home</a><a href="#">About Us</a><a href="#">Solutions</a><a href="#">Services</a>
</nav>

<div class="abs slider-frame"></div>
<div class="abs slider-shadow"></div>
<div class="abs slider-photo" role="img" aria-label="Photo of a businessman on the phone in front of server racks"></div>
<div class="abs caption">Managed IT Service<br>Professionals</div>
<div class="abs arrow" style="left:200px;top:232px"><svg width="10" height="14"><path d="M8 1L2 7l6 6" fill="none" stroke="#c4121a" stroke-width="2.5"/></svg></div>
<div class="abs arrow" style="left:979px;top:232px"><svg width="10" height="14"><path d="M2 1l6 6-6 6" fill="none" stroke="#c4121a" stroke-width="2.5"/></svg></div>

<section class="abs feature" style="left:177px;top:452px;width:175px">
  <h2>Spotlight</h2>
  <p>Keep your data secure and readily available with our online backup service</p>
</section>
<div class="abs feature-icon" style="left:369px;top:460px"><span><svg width="26" height="26"><circle cx="10" cy="10" r="6.5" fill="none" stroke="#111" stroke-width="3"/><path d="M14.5 14.5l8 8" stroke="#111" stroke-width="4" stroke-linecap="round"/></svg></span></div>
<div class="abs btn-more" style="left:175px;top:559px">Read More<span class="dot"><svg width="7" height="9"><path d="M1 1l4 3.5-4 3.5" fill="none" stroke="#fff" stroke-width="2"/></svg></span></div>
<div class="abs vrule" style="left:463px;top:457px;height:131px"></div>

<section class="abs feature" style="left:490px;top:452px;width:160px">
  <h2>Partners</h2>
  <p>We work with the best to bring<br>you the best.</p>
</section>
<div class="abs feature-icon" style="left:675px;top:460px"><span><svg width="30" height="26"><g fill="#111"><circle cx="6" cy="4" r="3"/><circle cx="15" cy="4" r="3"/><circle cx="24" cy="4" r="3"/><rect x="2" y="8" width="8" height="11" rx="2"/><rect x="11" y="8" width="8" height="11" rx="2"/><rect x="20" y="8" width="8" height="11" rx="2"/><rect x="3" y="18" width="6" height="8"/><rect x="12" y="18" width="6" height="8"/><rect x="21" y="18" width="6" height="8"/></g></svg></span></div>
<div class="abs btn-more" style="left:491px;top:559px">Read More<span class="dot"><svg width="7" height="9"><path d="M1 1l4 3.5-4 3.5" fill="none" stroke="#fff" stroke-width="2"/></svg></span></div>
<div class="abs vrule" style="left:770px;top:457px;height:131px"></div>

<section class="abs feature" style="left:793px;top:452px;width:170px">
  <h2>Live Support</h2>
  <p>Click here to access our Live support</p>
</section>
<div class="abs feature-icon" style="left:963px;top:460px"><span><svg width="28" height="28"><path d="M5 15a9 9 0 0 1 18 0" fill="none" stroke="#111" stroke-width="2.5"/><rect x="3" y="14" width="5" height="9" rx="2" fill="#111"/><rect x="20" y="14" width="5" height="9" rx="2" fill="#111"/><path d="M6 23q2 4 8 4" fill="none" stroke="#111" stroke-width="1.5"/></svg></span></div>

<div class="abs hrule" style="left:177px;top:611px;width:863px"></div>

<h2 class="abs section-title" style="left:177px;top:629px">Solutions</h2>
<p class="abs intro" style="left:177px;top:669px;width:480px">Our Enterprise solutions provide all businesses with professional answers without breaking the budget</p>
<ul class="abs service-list" style="left:176px;top:722px">
  <li><span class="dot"><svg width="7" height="9"><path d="M1 1l4 3.5-4 3.5" fill="none" stroke="#fff" stroke-width="2"/></svg></span>Managed Services</li>
  <li><span class="dot"><svg width="7" height="9"><path d="M1 1l4 3.5-4 3.5" fill="none" stroke="#fff" stroke-width="2"/></svg></span>Virtualization</li>
  <li><span class="dot"><svg width="7" height="9"><path d="M1 1l4 3.5-4 3.5" fill="none" stroke="#fff" stroke-width="2"/></svg></span>Backup</li>
  <li><span class="dot"><svg width="7" height="9"><path d="M1 1l4 3.5-4 3.5" fill="none" stroke="#fff" stroke-width="2"/></svg></span>Development</li>
  <li><span class="dot"><svg width="7" height="9"><path d="M1 1l4 3.5-4 3.5" fill="none" stroke="#fff" stroke-width="2"/></svg></span>Storage</li>
</ul>
<div class="abs network-art" role="img" aria-label="Illustration of a globe connected to laptop, desktop and servers"></div>
<div class="abs vrule" style="left:736px;top:641px;height:264px"></div>

<div class="abs card" style="left:767px;top:640px;width:270px;height:101px;overflow:hidden">
  <div class="portrait" role="img" aria-label="Photo of a smiling business technology expert"></div>
  <div style="position:absolute;left:15px;top:12px">
    <div class="card-title">Request a call</div>
    <small style="margin-top:5px">from one of our Business<br>Technology Experts today</small>
    <a href="#" style="display:block;margin-top:8px">Contact Us</a>
  </div>
</div>

<div class="abs card" style="left:767px;top:761px;width:270px;height:58px;display:flex;align-items:center">
  <svg width="34" height="24" style="margin:0 22px 0 18px"><rect x="1" y="1" width="32" height="22" fill="none" stroke="#c8c8c8"/><path d="M1 1l16 12L33 1M1 23l12-10M33 23L21 13" fill="none" stroke="#c8c8c8"/></svg>
  <span class="card-title">Sign up our newsletter</span>
</div>

<div class="abs card" style="left:767px;top:845px;width:270px;height:60px">
  <div class="social"><span class="label">Follow Us on</span><i><b></b></i><i><b></b></i><i><b></b></i><i><b></b></i></div>
</div>

<div class="abs hrule" style="left:177px;top:929px;width:863px"></div>

<h2 class="abs section-title" style="left:178px;top:948px;font-size:19px">Visit our Blog</h2>
<p class="abs" style="left:179px;top:974px;font-size:12px">Small Business Tech Tips</p>
<div class="abs news"><span class="tag">NEWS</span><svg width="6" height="8" style="margin:0 8px 0 17px"><path d="M0 0l5 4-5 4z" fill="#333"/></svg>Our Enterprise solutions provide all businesses with professional answers without breaking the budget</div>

<footer class="abs footer">
  <nav>Home<span>|</span>About Us<span>|</span>Services<span>|</span>Solutions<span>|</span>News<span>|</span>Contact Us</nav>
  <span>Copyrights @ 2012 All Rights Reserved</span>
</footer>

<div class="abs hrule" style="left:177px;top:1064px;width:863px"></div>
<div class="abs bottombar"></div>
</body>
</html>
```